Laboratory marketing Flyer

I want to create a flyer that's reflective of all the services our laboratory offers. please review our services at www.qorvantdiagnostics.com as well as about us for our amenities. focus more on areas of testing other than Toxicology, Covid-19 and Neutralizing anti-body titer. More so on UTI, Gastrointestinal, Wound, Genetics and respiratory. attached is a very old/outdated brochure, I want this in one page, vertical, front and back format.

Target Market(s)

medical facilities

Industry/Entity Type

medical

Font styles to use
Sans Serif

Colors
0054AA
0677BA
7BADD7
CADEEF
E8F1F8

Requirements
Must have
• Answer the phone, quick sample collection, fast turnaround time, large test menu, and Tarn-Ledger-Hub integration

```html
<!DOCTYPE html>
<html lang="en">
<head>
<meta charset="utf-8">
<title>Qorvant Diagnostics – Front and Back Flyer</title>
<link href="https://fonts.googleapis.com/css2?family=Outfit:wght@400;500;600;700;800;900&display=swap" rel="stylesheet">
<style>
  :root{
    --stage:#a2a7ab;
    --blue:#2a6fc7;
    --blue-deep:#0054aa;
    --blue-mid:#0677ba;
    --blue-soft:#7badd7;
    --blue-pale:#cadeef;
    --blue-wash:#eef4fa;
    --ink:#2f3033;
    --dark:#333538;
    --white:#ffffff;
  }
  *{box-sizing:border-box;margin:0;padding:0}
  html,body{width:1200px;height:800px;overflow:hidden;background:var(--stage)}
  body{font-family:'Outfit',sans-serif;color:var(--ink);position:relative}
  .page{position:absolute;width:523px;height:677px;background:var(--white);overflow:hidden}
  .page--front{left:67px;top:51px}
  .page--back{left:616px;top:51px;height:680px}
  .hero{position:absolute;left:0;top:0;width:100%;height:190px}
  .hero-title{position:absolute;left:0;right:0;text-align:center;color:var(--white);font-weight:900;font-size:37px;line-height:31px;letter-spacing:-.4px}
  .hero-sub{position:absolute;left:0;right:0;text-align:center;color:var(--white);font-size:11.5px;line-height:13.5px;font-weight:400}
  .brand-seal{position:absolute;width:74px;height:74px;border-radius:50%;background:var(--white);left:225px;top:146px}
  .brand-name{position:absolute;left:0;right:0;top:206px;text-align:center;font-weight:700;font-size:27px;color:var(--blue);letter-spacing:.2px;line-height:1}
  .brand-name small{display:block;font-size:12px;letter-spacing:6px;margin-top:4px}
  .lab-photo{position:absolute;left:41px;top:275px;width:218px;height:145px;background:linear-gradient(120deg,#dfeefa 0%,#a9cdea 45%,#5f8fb8 100%)}
  .intro{position:absolute;left:276px;top:274px;width:228px}
  .intro h2{font-size:13.2px;font-weight:800;color:var(--blue);line-height:1.2;margin-bottom:6px}
  .intro p{font-size:7.4px;line-height:1.28;color:var(--ink);margin-bottom:5px;font-weight:500}
  .benefits-band{position:absolute;left:0;top:461px;width:100%;height:152px;background:var(--blue-wash)}
  .benefits-title{position:absolute;left:40px;top:441px;font-size:23px;font-weight:900;color:var(--dark);letter-spacing:-.3px;line-height:1}
  .benefits-title span{color:var(--blue)}
  .benefits-rule{position:absolute;left:212px;top:459px;width:270px;height:1px;background:linear-gradient(90deg,var(--dark) 0 48%,transparent 48% 50%,var(--blue) 50%)}
  .benefit{position:absolute;top:478px;text-align:center;font-size:8.8px;line-height:1.25;font-weight:500;color:var(--ink);text-transform:uppercase}
  .benefit svg{display:block;margin:0 auto 4px}
  .v-dots{position:absolute;width:0;border-left:1.3px dotted var(--blue)}
  .amenities{position:absolute;left:304px;top:478px;width:212px}
  .amenities h3{font-size:12.5px;font-weight:700;color:var(--blue);margin-bottom:6px}
  .amenities li{list-style:none;font-size:8px;line-height:12.2px;color:var(--ink);display:flex;align-items:center;gap:4px;white-space:nowrap}
  .amenities li svg{flex:none}
  .footer{position:absolute;left:0;bottom:0;width:100%;height:64px}
  .footer-rule{position:absolute;left:0;top:0;width:100%;height:3px;background:var(--blue)}
  .footer-bar{position:absolute;left:0;top:5px;width:100%;height:59px;background:var(--dark)}
  .footer-cta{position:absolute;right:0;top:5px;width:208px;height:59px}
  .footer-address{position:absolute;left:33px;top:17px;color:var(--white);font-size:10.5px;font-weight:400}
  .footer-web{position:absolute;left:33px;top:34px;color:var(--white);font-size:12.5px;font-weight:600;display:flex;align-items:center;gap:6px}
  .footer-web i{display:inline-block;width:13px;height:13px;border-radius:50%;background:var(--white)}
  .footer-web b{font-weight:300;opacity:.8;margin-right:2px}
  .phone-badge{position:absolute;width:34px;height:34px;border-radius:50%;background:var(--white);display:flex;align-items:center;justify-content:center}
  .contact{position:absolute;color:var(--white);line-height:1}
  .contact em{font-style:normal;display:block;font-size:13.5px;font-weight:500;margin-bottom:6px}
  .contact strong{display:block;font-size:20.5px;font-weight:700}
  .services{position:absolute;left:0;top:0;width:100%;height:100%}
  .service{position:absolute;width:116px;margin-left:-58px;text-align:center;font-size:12.3px;line-height:1.22;font-weight:500;color:var(--ink)}
  .service svg{display:block;margin:0 auto 8px}
</style>
</head>
<body>

<svg width="0" height="0" style="position:absolute" aria-hidden="true">
  <defs>
    <symbol id="ring" viewBox="0 0 76 76">
      <circle cx="38" cy="38" r="33" fill="none" stroke="#2a6fc7" stroke-width="2.4"/>
      <path d="M66.6 21.5 A33 33 0 0 1 43.7 70.5" fill="none" stroke="#333538" stroke-width="3"/>
    </symbol>
    <symbol id="ring-s" viewBox="0 0 56 56">
      <circle cx="28" cy="28" r="25" fill="none" stroke="#2a6fc7" stroke-width="1.8"/>
      <path d="M49.6 15.5 A25 25 0 0 1 32.3 52.6" fill="none" stroke="#333538" stroke-width="2.3"/>
    </symbol>
    <symbol id="tick" viewBox="0 0 10 10">
      <path d="M5 .5 L9 2 V5 C9 7.5 7 9 5 9.6 C3 9 1 7.5 1 5 V2 Z" fill="#2a6fc7"/>
      <path d="M3.2 5 L4.6 6.4 L7 3.8" fill="none" stroke="#fff" stroke-width="1.1"/>
    </symbol>
    <symbol id="handset" viewBox="0 0 20 20">
      <path d="M5.5 2.5 L8 6.5 L6.3 8.3 C7.2 10.5 9.5 12.8 11.7 13.7 L13.5 12 L17.5 14.5 L15.8 17.5 C9.5 17.5 2.5 10.5 2.5 4.2 Z" fill="#333538"/>
    </symbol>
    <linearGradient id="heroTone" x1="0" y1="0" x2="1" y2="1">
      <stop offset="0" stop-color="#3a7fd0"/>
      <stop offset=".55" stop-color="#2a6cc2"/>
      <stop offset="1" stop-color="#3b82d4"/>
    </linearGradient>
  </defs>
</svg>

<!-- FRONT -->
<section class="page page--front">
  <svg class="hero" viewBox="0 0 523 190" role="img" aria-label="Blue-toned photograph of laboratory work with pipettes and sample plates">
    <polygon points="0,0 523,0 523,149 262,188 0,149" fill="url(#heroTone)"/>
  </svg>
  <h1 class="hero-title" style="top:40px">STATE-OF-THE-ART LAB<br>DIAGNOSTICS</h1>
  <p class="hero-sub" style="top:106px">GET FAST, PRECISE RESULTS THROUGH THE MOST<br>INNOVATIVE TESTING</p>
  <div class="brand-seal"></div>
  <div class="brand-name">QORVANT<small>DIAGNOSTICS</small></div>

  <div class="lab-photo" role="img" aria-label="Photograph of scientists in lab coats working with microscopes and blue sample tubes"></div>
  <div class="intro">
    <h2>WE PROVIDE TRUSTED RESULTS THROUGH THE MOST INNOVATIVE TESTING METHODS</h2>
    <p>At Qorvant we strive to give physicians, hospitals, medical centers, clinics and healthcare facilities fast, precise molecular testing, from urinary tract infection, gastrointestinal and respiratory pathogen panels to wound care and genetic testing.</p>
    <p>We answer the phone, arrange quick sample collection and deliver a fast turnaround time across a large test menu. Results flow straight into your Tarn-Ledger-Hub system, so your practice can act sooner and guide better care for your patients.</p>
  </div>

  <div class="benefits-band"></div>
  <h2 class="benefits-title">OUR <span>BENEFITS</span></h2>
  <div class="benefits-rule"></div>

  <div class="benefit" style="left:22px;width:104px">
    <svg width="56" height="56" viewBox="0 0 56 56">
      <use href="#ring-s"/>
      <path d="M19 15 H32 L38 21 V41 H19 Z" fill="#2a6fc7"/>
      <rect x="23" y="31" width="3" height="6" fill="#fff"/><rect x="27.5" y="27" width="3" height="10" fill="#fff"/><rect x="32" y="29" width="3" height="8" fill="#fff"/>
    </svg>
    PRECISE RESULTS THROUGH THE MOST INNOVATIVE TECHNOLOGY
  </div>
  <div class="v-dots" style="left:121px;top:482px;height:52px"></div>
  <div class="benefit" style="left:126px;width:78px">
    <svg width="56" height="56" viewBox="0 0 56 56">
      <use href="#ring-s"/>
      <circle cx="28" cy="30" r="10" fill="none" stroke="#2a6fc7" stroke-width="3.2"/>
      <path d="M28 30 L32 24" stroke="#2a6fc7" stroke-width="2.6" stroke-linecap="round"/>
      <rect x="25" y="15" width="6" height="3" fill="#2a6fc7"/>
    </svg>
    FAST<br>TURNAROUND
  </div>
  <div class="v-dots" style="left:206px;top:482px;height:52px"></div>
  <div class="benefit" style="left:205px;width:78px">
    <svg width="56" height="56" viewBox="0 0 56 56">
      <use href="#ring-s"/>
      <rect x="18" y="15" width="9" height="24" rx="4.5" fill="#2a6fc7"/>
      <circle cx="34" cy="34" r="7" fill="#2a6fc7"/>
      <path d="M30.5 34 L33 36.5 L37.5 31.5" fill="none" stroke="#fff" stroke-width="1.8"/>
    </svg>
    LARGE<br>TEST<br>MENU
  </div>

  <div class="amenities">
    <h3>OUR AMENITIES</h3>
    <ul>
      <li><svg width="9" height="9"><use href="#tick"/></svg>We answer the phone, every call, every day</li>
      <li><svg width="9" height="9"><use href="#tick"/></svg>Quick sample collection and pick-up services</li>
      <li><svg width="9" height="9"><use href="#tick"/></svg>Fast turnaround time on every panel</li>
      <li><svg width="9" height="9"><use href="#tick"/></svg>A large test menu: UTI, GI, wound and genetics</li>
      <li><svg width="9" height="9"><use href="#tick"/></svg>Tarn-Ledger-Hub integration for your results</li>
      <li><svg width="9" height="9"><use href="#tick"/></svg>Simple, easy-to-read and time sensible reports</li>
    </ul>
  </div>

  <footer class="footer">
    <div class="footer-rule"></div>
    <div class="footer-bar"></div>
    <svg class="footer-cta" viewBox="0 0 208 59" preserveAspectRatio="none"><polygon points="30,0 208,0 208,59 0,59" fill="#2a6fc7"/></svg>
    <p class="footer-address">4170 Larkmoor Pkwy, Suite 210 Eastbrook, MI 48120</p>
    <p class="footer-web">www.qorvantdiagnostics.com <b>|</b><i></i><i></i><i></i></p>
    <div class="phone-badge" style="left:317px;top:18px"><svg width="20" height="20"><use href="#handset"/></svg></div>
    <p class="contact" style="left:365px;top:17px"><em>Contact us Today!</em><strong>(555) 014-2290</strong></p>
  </footer>
</section>

<!-- BACK -->
<section class="page page--back">
  <svg class="hero" viewBox="0 0 523 190" role="img" aria-label="Blue-toned photograph of gloved hands handling sample tubes">
    <polygon points="0,0 523,0 523,149 262,188 0,149" fill="url(#heroTone)"/>
  </svg>
  <h1 class="hero-title" style="top:40px">OUR SERVICES</h1>
  <p class="hero-sub" style="top:79px">GET FAST, PRECISE RESULTS THROUGH THE MOST<br>INNOVATIVE TESTING</p>
  <div class="brand-seal"></div>

  <div class="services">
    <div class="v-dots" style="left:146px;top:217px;height:100px"></div>
    <div class="v-dots" style="left:250px;top:217px;height:100px"></div>
    <div class="v-dots" style="left:357px;top:217px;height:100px"></div>
    <div class="v-dots" style="left:146px;top:356px;height:100px"></div>
    <div class="v-dots" style="left:250px;top:356px;height:100px"></div>
    <div class="v-dots" style="left:357px;top:356px;height:100px"></div>
    <div class="v-dots" style="left:215px;top:498px;height:100px"></div>
    <div class="v-dots" style="left:318px;top:498px;height:100px"></div>

    <div class="service" style="left:90px;top:218px">
      <svg width="72" height="72" viewBox="0 0 76 76"><use href="#ring"/>
        <rect x="23" y="19" width="30" height="3" fill="#2a6fc7"/>
        <rect x="25" y="25" width="26" height="29" fill="#2a6fc7"/>
        <rect x="25" y="30" width="7" height="2" fill="#fff"/><rect x="25" y="36" width="5" height="2" fill="#fff"/><rect x="25" y="42" width="7" height="2" fill="#fff"/><rect x="25" y="48" width="5" height="2" fill="#fff"/>
      </svg>Urinary Tract<br>Infection qPCR</div>

    <div class="service" style="left:197px;top:218px">
      <svg width="72" height="72" viewBox="0 0 76 76"><use href="#ring"/>
        <path d="M32 18 V28 C32 32 36 32 40 30 C50 26 56 34 52 44 C48 53 36 55 28 50 L24 56 L20 53 L25 46 C28 42 34 44 38 42" fill="none" stroke="#2a6fc7" stroke-width="5" stroke-linejoin="round"/>
      </svg>Gastrointestinal<br>Panel</div>

    <div class="service" style="left:303px;top:218px">
      <svg width="72" height="72" viewBox="0 0 76 76"><use href="#ring"/>
        <path d="M35 30 C27 24 18 34 19 46 C20 52 28 52 35 47 Z" fill="#2a6fc7"/>
        <path d="M41 30 C49 24 58 34 57 46 C56 52 48 52 41 47 Z" fill="#2a6fc7"/>
        <rect x="36.5" y="18" width="3" height="18" fill="#2a6fc7"/>
        <circle cx="38" cy="40" r="4" fill="#fff"/>
      </svg>Respiratory<br>Pathogen<br>Panel (RPP)</div>

    <div class="service" style="left:420px;top:218px">
      <svg width="72" height="72" viewBox="0 0 76 76"><use href="#ring"/>
        <rect x="15" y="28" width="46" height="20" rx="4" fill="#2a6fc7"/>
        <rect x="28" y="28" width="20" height="20" fill="#fff"/>
        <rect x="30" y="30" width="16" height="16" fill="#2a6fc7"/>
        <circle cx="35" cy="35" r="1.4" fill="#fff"/><circle cx="41" cy="35" r="1.4" fill="#fff"/><circle cx="35" cy="41" r="1.4" fill="#fff"/><circle cx="41" cy="41" r="1.4" fill="#fff"/>
      </svg>Wound Panel</div>

    <div class="service" style="left:90px;top:355px">
      <svg width="72" height="72" viewBox="0 0 76 76"><use href="#ring"/>
        <rect x="24" y="18" width="28" height="4" fill="#2a6fc7"/><rect x="24" y="52" width="28" height="4" fill="#2a6fc7"/>
        <path d="M27 22 H49 L32 52 H27 Z M49 52 H44 L41 46 H49 Z" fill="#2a6fc7"/>
        <rect x="31" y="33" width="14" height="2.4" fill="#2a6fc7"/><rect x="31" y="40" width="14" height="2.4" fill="#2a6fc7"/>
      </svg>Genetic Testing</div>

    <div class="service" style="left:197px;top:355px">
      <svg width="72" height="72" viewBox="0 0 76 76"><use href="#ring"/>
        <circle cx="38" cy="30" r="10" fill="none" stroke="#2a6fc7" stroke-width="5"/>
        <rect x="35.5" y="40" width="5" height="16" fill="#2a6fc7"/><rect x="30" y="46" width="16" height="4.5" fill="#2a6fc7"/>
      </svg>Women’s<br>Health qPCR</div>

    <div class="service" style="left:303px;top:355px">
      <svg width="72" height="72" viewBox="0 0 76 76"><use href="#ring"/>
        <circle cx="31" cy="32" r="8" fill="#2a6fc7"/><circle cx="31" cy="32" r="12" fill="none" stroke="#2a6fc7" stroke-width="3" stroke-dasharray="3 3"/>
        <circle cx="48" cy="45" r="5.5" fill="#2a6fc7"/><circle cx="48" cy="45" r="8.5" fill="none" stroke="#2a6fc7" stroke-width="2.6" stroke-dasharray="2.5 2.5"/>
      </svg>Sexually<br>Transmitted<br>Infections (STI)</div>

    <div class="service" style="left:420px;top:355px">
      <svg width="72" height="72" viewBox="0 0 76 76"><use href="#ring"/>
        <ellipse cx="30" cy="33" rx="10" ry="7" transform="rotate(-35 30 33)" fill="#2a6fc7"/>
        <ellipse cx="46" cy="44" rx="10" ry="7" transform="rotate(-35 46 44)" fill="#2a6fc7"/>
        <circle cx="28" cy="32" r="1.8" fill="#fff"/><circle cx="33" cy="35" r="1.5" fill="#fff"/><circle cx="44" cy="43" r="1.8" fill="#fff"/><circle cx="49" cy="46" r="1.5" fill="#fff"/>
      </svg>Infectious<br>Diseases</div>

    <div class="service" style="left:161px;top:499px">
      <svg width="72" height="72" viewBox="0 0 76 76"><use href="#ring"/>
        <rect x="23" y="21" width="11" height="33" rx="5.5" fill="#2a6fc7"/><rect x="41" y="21" width="11" height="33" rx="5.5" fill="#2a6fc7"/>
        <rect x="21" y="20" width="15" height="4" fill="#2a6fc7"/><rect x="39" y="20" width="15" height="4" fill="#2a6fc7"/>
        <rect x="26" y="28" width="5" height="14" fill="#fff" opacity=".5"/><rect x="44" y="28" width="5" height="14" fill="#fff" opacity=".5"/>
      </svg>Blood Testing</div>

    <div class="service" style="left:268px;top:499px">
      <svg width="72" height="72" viewBox="0 0 76 76"><use href="#ring"/>
        <rect x="28" y="22" width="5" height="20" rx="2.5" fill="#2a6fc7"/><rect x="34" y="18" width="5" height="24" rx="2.5" fill="#2a6fc7"/>
        <rect x="40" y="19" width="5" height="23" rx="2.5" fill="#2a6fc7"/><rect x="46" y="23" width="5" height="20" rx="2.5" fill="#2a6fc7"/>
        <path d="M27 38 H51 V46 C51 53 45 57 39 57 C33 57 27 53 22 45 L20 40 C22 38 25 39 27 42 Z" fill="#2a6fc7"/>
      </svg>Nail Panel</div>

    <div class="service" style="left:375px;top:499px">
      <svg width="72" height="72" viewBox="0 0 76 76"><use href="#ring"/>
        <path d="M26 25 H36 V33 L44 50 H18 L26 33 Z" fill="#2a6fc7"/>
        <path d="M31 38 L35 45 H27 Z" fill="#fff"/>
        <circle cx="51" cy="22" r="5" fill="#2a6fc7"/>
        <rect x="45" y="34" width="12" height="2" fill="#2a6fc7"/><rect x="45" y="39" width="12" height="2" fill="#2a6fc7"/><rect x="45" y="44" width="12" height="2" fill="#2a6fc7"/>
      </svg>Toxicology Testing</div>
  </div>

  <footer class="footer" style="height:66px">
    <div class="footer-rule"></div>
    <div class="footer-bar" style="top:6px;height:60px"></div>
    <svg class="footer-cta" style="top:6px;height:60px;width:208px" viewBox="0 0 208 60" preserveAspectRatio="none"><polygon points="30,0 208,0 208,60 0,60" fill="#2a6fc7"/></svg>
    <p class="footer-address" style="top:19px">4170 Larkmoor Pkwy, Suite 210 Eastbrook, MI 48120</p>
    <p class="footer-web" style="top:36px">www.qorvantdiagnostics.com <b>|</b><i></i><i></i><i></i></p>
    <div class="phone-badge" style="left:318px;top:20px"><svg width="20" height="20"><use href="#handset"/></svg></div>
    <p class="contact" style="left:366px;top:19px"><em>Contact us Today!</em><strong>(555) 014-2290</strong></p>
  </footer>
</section>

</body>
</html>
```